iPhone iOS 7 App For Managing Tasks/Photos for Internal Company Use

We need an app design that displays company objectives and task, and provides the interface for employees to complete a task by uploading a photo and adding comments.

Please see attached mock up sketches as a rough guideline

Final delivery of files must contain PSD, and all layers/objects sliced both is PSD and PNG files

Target Market(s)

This is a tool for internal employee use

Industry/Entity Type

It Company

Requirements
Must have
• Must include logo, and match the colour scheme
Use iPhone iOS 7 Style

```html
<!DOCTYPE html>
<html lang="en">
<head>
<meta charset="utf-8">
<title>My Progress</title>
<link rel="stylesheet" href="https://fonts.googleapis.com/css2?family=Roboto:wght@300;400;500;700&display=swap">
<style>
  :root {
    --backdrop: #262626;
    --status-bar: #6d93ae;
    --nav-top: #6f98b4;
    --nav-bottom: #7ea6c0;
    --body-top: #9fc1d4;
    --body-bottom: #5e889f;
    --ring-dark: #4b7096;
    --ring-light: #ffffff;
    --text-light: #ffffff;
    --tab-bg: #ffffff;
    --tab-text: #4a4a4a;
    --tab-active: #3f6e9c;
    --tab-line: #d9dde0;
  }
  * { box-sizing: border-box; margin: 0; padding: 0; }
  html, body {
    width: 1200px; height: 865px; overflow: hidden;
    background: var(--backdrop);
    font-family: "Roboto", "Helvetica Neue", Arial, sans-serif;
  }
  .app-screen {
    position: absolute; left: 375px; top: 32px;
    width: 450px; height: 800px;
    background: linear-gradient(180deg, var(--body-top) 0%, var(--body-bottom) 100%);
    overflow: hidden; color: var(--text-light);
  }
  .status-bar {
    height: 22px; background: var(--status-bar);
    display: flex; align-items: center; justify-content: space-between;
    padding: 0 8px; font-size: 12px;
  }
  .status-carrier { display: flex; align-items: center; gap: 5px; }
  .signal { display: flex; gap: 2px; }
  .signal span { width: 6px; height: 6px; border-radius: 50%; border: 1px solid #fff; }
  .signal span.on { background: #fff; }
  .status-battery { display: flex; align-items: center; gap: 5px; }
  .battery { width: 22px; height: 10px; border: 1px solid #fff; border-radius: 2px; padding: 1px; position: relative; }
  .battery::after { content: ""; position: absolute; right: -3px; top: 2px; width: 2px; height: 4px; background: #fff; }
  .battery span { display: block; width: 50%; height: 100%; background: #fff; }
  .nav-bar {
    height: 58px; position: relative;
    background: linear-gradient(180deg, var(--nav-top), var(--nav-bottom));
    display: flex; align-items: center; justify-content: center;
  }
  .nav-title { font-size: 22px; font-weight: 400; }
  .back-button {
    position: absolute; left: 14px; top: 11px;
    width: 56px; height: 36px; border: 1px solid rgba(255,255,255,.7); border-radius: 4px;
    display: flex; align-items: center; justify-content: center;
  }
  .progress-ring { position: absolute; left: 115px; top: 120px; width: 220px; height: 220px; }
  .ring-label {
    position: absolute; left: 115px; top: 120px; width: 220px; height: 220px;
    display: flex; flex-direction: column; align-items: center; justify-content: center;
  }
  .ring-value { font-size: 64px; font-weight: 700; line-height: 1; }
  .ring-caption { font-size: 20px; font-weight: 400; margin-top: 2px; }
  .objectives-summary {
    position: absolute; left: 0; top: 390px; width: 100%;
    text-align: center; font-size: 46px; font-weight: 300; line-height: 1.2;
  }
  .tab-bar {
    position: absolute; left: 0; bottom: 0; width: 100%; height: 68px;
    background: var(--tab-bg); border-top: 1px solid var(--tab-line);
    display: flex;
  }
  .tab-item {
    flex: 1; display: flex; flex-direction: column; align-items: center; justify-content: center;
    gap: 4px; font-size: 13px; color: var(--tab-text);
  }
  .tab-item.is-active { color: var(--tab-active); }
</style>
</head>
<body>
<main class="app-screen">
  <div class="status-bar">
    <div class="status-carrier">
      <div class="signal"><span class="on"></span><span class="on"></span><span></span><span></span><span></span></div>
      <span>ORL</span>
      <svg width="14" height="10" viewBox="0 0 14 10"><path d="M1 4a9 9 0 0 1 12 0M3.5 6a5 5 0 0 1 7 0" fill="none" stroke="#fff" stroke-width="1.4"/><circle cx="7" cy="8.5" r="1.2" fill="#fff"/></svg>
    </div>
    <span class="status-time">5:17 PM</span>
    <div class="status-battery"><span>50 %</span><div class="battery"><span></span></div></div>
  </div>

  <header class="nav-bar">
    <div class="back-button">
      <svg width="24" height="14" viewBox="0 0 24 14"><path d="M22 7H4M9 2L3 7l6 5" fill="none" stroke="#fff" stroke-width="2.4"/></svg>
    </div>
    <h1 class="nav-title">My Progress</h1>
  </header>

  <svg class="progress-ring" viewBox="0 0 220 220">
    <circle cx="110" cy="110" r="96" fill="none" stroke="var(--ring-light)" stroke-width="22"/>
    <circle cx="110" cy="110" r="96" fill="none" stroke="var(--ring-dark)" stroke-width="22"
            stroke-dasharray="386 217" transform="rotate(-90 110 110)"/>
  </svg>
  <div class="ring-label">
    <span class="ring-value">64%</span>
    <span class="ring-caption">completeness</span>
  </div>

  <p class="objectives-summary">10/10 Objectives<br>Complete</p>

  <nav class="tab-bar">
    <div class="tab-item">
      <svg width="28" height="24" viewBox="0 0 28 24"><path d="M3 12L14 3l11 9M6 10v12h16V10M11 22v-7h6v7M20 5v3" fill="none" stroke="currentColor" stroke-width="1.4"/></svg>
      <span>Home</span>
    </div>
    <div class="tab-item is-active">
      <svg width="28" height="26" viewBox="0 0 28 26"><circle cx="14" cy="13" r="11" fill="none" stroke="currentColor" stroke-width="1.4" stroke-dasharray="14 3"/><circle cx="14" cy="13" r="6" fill="none" stroke="currentColor" stroke-width="1.4"/></svg>
      <span>Obejectives</span>
    </div>
    <div class="tab-item">
      <svg width="30" height="24" viewBox="0 0 30 24"><rect x="4" y="2" width="23" height="20" fill="none" stroke="currentColor" stroke-width="1.6"/><path d="M4 8H1v12a2 2 0 0 0 3 2M8 6h7v6H8zM18 6h6M18 9h6M18 12h6M8 15h16M8 18h16" fill="none" stroke="currentColor" stroke-width="1.4"/></svg>
      <span>News</span>
    </div>
    <div class="tab-item">
      <svg width="28" height="24" viewBox="0 0 28 24"><path d="M18 8V3H3v18h15v-5M10 12h15M21 8l4 4-4 4" fill="none" stroke="currentColor" stroke-width="1.6"/></svg>
      <span>Logout</span>
    </div>
  </nav>
</main>
</body>
</html>
```